Namibia currently imports 60% of its food. Meridale Field Trust is an initiative which will assist Namibia to become self sustainable in terms of food production. We aim to do this through the development of 3 agricultural production zones which will include farming zones, local farmer assistance, processing and distribution of the final products. Please see our project overview attached.

```html
<!DOCTYPE html>
<html lang="en">
<head>
<meta charset="utf-8">
<title>Meridale Field Trust</title>
<link href="https://fonts.googleapis.com/css2?family=Cinzel:wght@400;500&family=Poppins:wght@400;500;600;700;800&display=swap" rel="stylesheet">
<style>
:root{
  --green:#0b6b35;
  --green-dark:#08552a;
  --green-deep:#0e5e2e;
  --tan:#c9a886;
  --blue:#2aa7df;
  --grey-bg:#eeeeee;
  --text:#333;
  --muted:#555;
  --footer:#111;
  --white:#fff;
}
*{box-sizing:border-box;margin:0;padding:0}
html,body{width:1200px;height:5254px;overflow:hidden}
body{font-family:"Poppins",sans-serif;color:var(--text);background:var(--white);position:relative}
.wrap{width:918px;margin:0 auto;position:relative}
.btn{display:inline-block;background:var(--green);color:var(--white);font-size:13px;padding:0 24px;line-height:40px;border-radius:3px}
.section-title{font-family:"Cinzel",serif;font-size:38px;font-weight:400;text-align:center;color:#1a1a1a;letter-spacing:1px}
.section-lead{font-size:13px;text-align:center;line-height:23px;color:var(--text)}

/* top bar */
.topbar{height:29px;background:var(--green);color:var(--white);font-size:12px}
.topbar .wrap{display:flex;justify-content:space-between;align-items:center;height:29px}
.socials{display:flex;gap:8px}
.socials span{width:11px;height:11px;border-radius:50%;background:var(--white);display:block}
.contact-top{display:flex;gap:24px;align-items:center}
.contact-top div{display:flex;gap:6px;align-items:center}

/* nav */
.nav{height:77px;background:var(--white)}
.nav .wrap{display:flex;justify-content:space-between;align-items:center;height:77px}
.brand{font-size:20px;font-weight:600;color:var(--green);display:flex;align-items:center;gap:8px}
.brand i{width:14px;height:14px;border-radius:50%;background:var(--green);display:block}
.menu{display:flex;gap:24px;font-size:13px;align-items:center}
.menu .active{color:var(--green);font-weight:600}

/* hero */
.hero{height:529px;position:relative;background:linear-gradient(90deg,#2f3a22 0%,#4c5a32 40%,#7b8a55 70%,#9aa36a 100%)}
.hero-text{position:absolute;left:145px;top:90px;color:var(--white)}
.hero-text h1{font-family:"Cinzel",serif;font-weight:400;font-size:52px;line-height:56px;letter-spacing:1.5px}
.hero-text p{font-size:14px;margin:10px 0 26px}

/* mission */
.mvv{height:339px;background:var(--grey-bg);padding-top:59px}
.mvv-cards{display:flex;background:var(--white);height:222px}
.mvv-card{flex:1;padding:36px 30px;border-right:1px solid #e2e2e2}
.mvv-card:last-child{border-right:none}
.mvv-card svg{margin-bottom:16px}
.mvv-card h3{font-family:"Cinzel",serif;font-weight:500;font-size:17px;margin-bottom:10px;letter-spacing:.5px}
.mvv-card p{font-size:12px;line-height:22px;color:var(--muted)}

/* about */
.about{height:665px;padding-top:105px}
.about .section-lead{margin:14px 0 24px}
.about-row{display:flex;gap:64px;align-items:flex-start}
.about-text{padding-top:40px;width:440px;font-size:12.5px;line-height:23px;color:var(--text)}
.about-text p{margin-bottom:9px}
.about-text .btn{margin-top:18px}

/* projects */
.projects{height:731px;background:var(--grey-bg);padding-top:105px}
.projects .section-lead{margin:10px 0 22px}
.proj-cards{display:flex;gap:24px}
.proj-card{width:290px;height:370px;background:var(--white)}
.proj-card .body{padding:20px 20px}
.proj-card h3{font-family:"Cinzel",serif;font-weight:500;font-size:17px;line-height:22px;margin-bottom:12px}
.proj-card p{font-size:12px;line-height:22px;color:var(--muted);margin-bottom:18px}
.link{font-size:12px;font-weight:600;color:var(--green-dark);text-decoration:underline}
.arrow{position:absolute;width:38px;height:38px;border-radius:50%;background:var(--white);box-shadow:0 1px 4px rgba(0,0,0,.2);display:flex;align-items:center;justify-content:center}
.center{text-align:center}

/* reviews */
.reviews{height:420px;display:flex}
.reviews .half{width:600px;height:420px}
.review-panel{background:var(--green);color:var(--white);padding:110px 140px 0 58px;position:relative;overflow:hidden}
.review-panel h2{font-family:"Cinzel",serif;font-weight:400;font-size:34px;letter-spacing:1px;margin-bottom:12px}
.review-panel p{font-size:12.5px;line-height:23px}
.reviewer{display:flex;align-items:center;gap:12px;margin-top:22px}
.avatar{width:50px;height:50px;border-radius:50%;background:#c9b59a;border:3px solid var(--white)}
.reviewer b{display:block;font-size:14px}
.stars{color:#f5b800;font-size:14px;letter-spacing:1px}

/* zones */
.zones{height:580px;position:relative}
.zones-text{position:absolute;left:141px;top:130px;width:440px}
.zones-text h2{font-family:"Cinzel",serif;font-weight:400;font-size:36px;line-height:38px;letter-spacing:1px;color:#1a1a1a}
.zones-text .lead{font-size:12.5px;line-height:22px;margin:6px 0 20px}
.legend li{list-style:none;display:flex;align-items:center;gap:10px;font-size:15px;font-weight:500;margin-bottom:24px}
.legend i{width:18px;height:18px;display:block}
.map{position:absolute;left:661px;top:88px}

/* stats */
.stats{height:336px;display:flex;gap:6px}
.stat{flex:1;position:relative;color:var(--white);text-align:center}
.stat .num{position:absolute;top:90px;width:100%;font-size:92px;font-weight:800;color:rgba(255,255,255,.85);line-height:1}
.stat .label{position:absolute;top:200px;width:100%;font-size:19px;font-weight:600}

/* news */
.news{height:801px;padding-top:113px}
.news .section-lead{margin:8px 0 28px}
.news-cards{display:flex;gap:24px}
.news-card{width:290px;height:440px;border:1px solid #e2e2e2;background:var(--white)}
.news-card .body{padding:22px 28px}
.date{font-size:11.5px;color:var(--muted);margin-bottom:12px}
.news-card h4{font-size:13px;font-weight:600;line-height:22px;margin-bottom:10px}
.news-card p{font-size:12px;line-height:21px;color:var(--muted);margin-bottom:14px}

/* newsletter */
.newsletter{height:404px}
.nl-box{position:relative;width:918px;height:316px;margin:0 auto;background:linear-gradient(90deg,#0d6b33 0%,#1d7a35 55%,#3f8a36 100%);color:var(--white);padding:92px 72px;overflow:hidden}
.nl-art{position:absolute;right:0;top:0;width:420px;height:316px;background:linear-gradient(90deg,rgba(90,150,60,0) 0%,rgba(110,165,60,.45) 45%,rgba(150,185,70,.55) 100%)}
.nl-content{position:relative}
.nl-box h2{font-family:"Cinzel",serif;font-weight:400;font-size:34px;letter-spacing:1px}
.nl-box p{font-size:12.5px;line-height:22px;margin:10px 0 16px;width:440px}
.nl-form{display:flex;gap:6px}
.nl-form .input{width:304px;height:40px;background:var(--white);color:#222;font-size:12px;padding:0 24px;line-height:40px}
.nl-form .sub{width:126px;height:40px;background:var(--tan);font-size:12px;text-align:center;line-height:40px}

/* footer */
.footer{height:306px;background:var(--footer);color:var(--white);position:relative}
.footer h5{font-family:"Cinzel",serif;font-weight:400;font-size:17px;letter-spacing:1px;margin-bottom:12px}
.quick{position:absolute;left:141px;top:58px}
.quick li{list-style:none;font-size:12px;line-height:28px}
.foot-brand{position:absolute;left:420px;top:120px;width:360px;text-align:center;font-size:26px;font-weight:600;color:var(--green);display:flex;justify-content:center;align-items:center;gap:10px}
.foot-brand i{width:18px;height:18px;background:var(--green);border-radius:50%;display:block}
.contact{position:absolute;left:824px;top:58px;width:240px}
.contact .row{display:flex;gap:12px;font-size:12px;line-height:20px;margin-bottom:20px}
.contact .ico{width:28px;height:28px;background:#333;border-radius:3px;flex:none;display:flex;align-items:center;justify-content:center}
.bottom{height:37px;background:var(--green);color:var(--white);font-size:12px}
.bottom .wrap{display:flex;justify-content:space-between;align-items:center;height:37px}
</style>
</head>
<body>

<header>
  <div class="topbar">
    <div class="wrap">
      <div class="socials" aria-label="Social links"><span></span><span></span><span></span><span></span></div>
      <div class="contact-top">
        <div>
          <svg width="13" height="10" viewBox="0 0 13 10"><rect x="0.5" y="0.5" width="12" height="9" fill="none" stroke="#fff"/><path d="M1 1l5.5 4.5L12 1" fill="none" stroke="#fff"/></svg>
          info@meridalefieldtrust.org
        </div>
        <div>
          <svg width="12" height="12" viewBox="0 0 12 12"><path d="M2 1l2 0 1 3-1.5 1a7 7 0 0 0 3.5 3.5L8 7l3 1v2a1 1 0 0 1-1 1A9 9 0 0 1 1 2a1 1 0 0 1 1-1z" fill="none" stroke="#fff"/></svg>
          555-014-2290
        </div>
      </div>
    </div>
  </div>
  <nav class="nav">
    <div class="wrap">
      <div class="brand"><i></i>Meridale Field Trust</div>
      <div class="menu">
        <span class="active">Home</span><span>About Us</span><span>Our Projects</span><span>Farmer Resources</span><span>News &amp; Updates</span>
        <span class="btn">Contact Us</span>
      </div>
    </div>
  </nav>
</header>

<section class="hero" role="img" aria-label="Photo of two smiling women harvesting leafy greens in a field">
  <div class="hero-text">
    <h1>EMPOWERING<br>NAMIBIA TO<br>ACHIEVE FOOD<br>INDEPENDENCE</h1>
    <p>Reducing imports by fostering local agricultural production</p>
    <span class="btn">Learn About Our Projects</span>
  </div>
</section>

<section class="mvv">
  <div class="wrap mvv-cards">
    <div class="mvv-card">
      <svg width="42" height="42" viewBox="0 0 42 42"><circle cx="21" cy="21" r="18" fill="none" stroke="#333" stroke-width="2"/><circle cx="21" cy="21" r="10" fill="none" stroke="#333" stroke-width="2"/><circle cx="21" cy="21" r="3" fill="var(--green)"/><path d="M21 21l14-14" stroke="var(--green)" stroke-width="2"/></svg>
      <h3>OUR MISSION</h3>
      <p>Lorem ipsum dolor sit amet, dolor ex consectetur adipiscing elit, sed do ut eiusmod tempor.</p>
    </div>
    <div class="mvv-card">
      <svg width="42" height="42" viewBox="0 0 42 42"><circle cx="21" cy="11" r="6" fill="none" stroke="#333" stroke-width="2"/><circle cx="10" cy="26" r="5" fill="none" stroke="#333" stroke-width="2"/><circle cx="32" cy="26" r="5" fill="none" stroke="#333" stroke-width="2"/><path d="M2 40a8 8 0 0 1 16 0M24 40a8 8 0 0 1 16 0" fill="none" stroke="var(--green)" stroke-width="2"/></svg>
      <h3>OUR VISION</h3>
      <p>Lorem ipsum dolor sit amet, dolor ex consectetur adipiscing elit, sed do ut eiusmod tempor.</p>
    </div>
    <div class="mvv-card">
      <svg width="42" height="42" viewBox="0 0 42 42"><circle cx="21" cy="14" r="8" fill="none" stroke="#333" stroke-width="2"/><path d="M21 10v8M17 14h8" stroke="var(--green)" stroke-width="2"/><path d="M4 28l10 8h14l10-8" fill="none" stroke="#333" stroke-width="2"/></svg>
      <h3>OUR VALUES</h3>
      <p>Lorem ipsum dolor sit amet, dolor ex consectetur adipiscing elit, sed do ut eiusmod tempor.</p>
    </div>
  </div>
</section>

<section class="about">
  <div class="wrap">
    <h2 class="section-title">ABOUT US</h2>
    <p class="section-lead">Lorem ipsum dolor sit amet, consectetur adipiscing elit, sed do eiusmod tempor incididunt ut labore et dolore magna aliqua. Ut enim ad<br>minim veniam, quis nostrud exercitation ullamco laboris nisi ut aliquip ex ea commodo consequat.</p>
    <div class="about-row">
      <div role="img" aria-label="Photo of freshly harvested potatoes on soil beside rows of potato plants" style="width:414px;height:353px;background:linear-gradient(180deg,#3e7a2a 0%,#2f5e22 35%,#5a3f2a 60%,#3d2a1c 100%)"></div>
      <div class="about-text">
        <p>Lorem Ipsum is simply dummy text of the printing and typesetting industry. Lorem Ipsum has been the industry's standard dummy text ever since the 1500s, when an unknown printer took a galley of type and scrambled it to make a type specimen book.</p>
        <p>It is a long established fact that a reader will be distracted by the readable content of a page when looking at its layout.</p>
        <p>Lorem ipsum dolor sit amet, consectetur adipiscing elit, sed do eiusmod tempor incididunt ut labore et dolore magna aliqua.</p>
        <span class="btn">Read More</span>
      </div>
    </div>
  </div>
</section>

<section class="projects">
  <div class="wrap">
    <h2 class="section-title">OUR PROJECTS</h2>
    <p class="section-lead">Ut enim ad minim veniam, quis nostrud exercitation ullamco laboris nisi ut aliquip ex ea commodo consequat.</p>
    <div class="arrow" style="left:-66px;top:330px"><svg width="10" height="12" viewBox="0 0 10 12"><path d="M7 1L2 6l5 5" fill="none" stroke="#111" stroke-width="2"/></svg></div>
    <div class="arrow" style="right:-66px;top:330px"><svg width="10" height="12" viewBox="0 0 10 12"><path d="M3 1l5 5-5 5" fill="none" stroke="#111" stroke-width="2"/></svg></div>
    <div class="proj-cards">
      <article class="proj-card">
        <div role="img" aria-label="Photo of a wheat field with solar panels under a blue sky" style="height:186px;background:linear-gradient(180deg,#5b8fd1 0%,#9cc0e6 30%,#7fa860 45%,#5c8a35 100%)"></div>
        <div class="body"><h3>AGRICULTURAL<br>PRODUCTION ZONES</h3><p>Lorem Ipsum is simply dummy text of the printing and typesetting industry.</p><span class="link">Read More</span></div>
      </article>
      <article class="proj-card">
        <div role="img" aria-label="Photo of a farmer checking a tablet among tall maize plants" style="height:186px;background:linear-gradient(90deg,#4d7a2c 0%,#8fb04a 50%,#3f6a24 100%)"></div>
        <div class="body"><h3>LOCAL FARMER<br>ASSISTANCE</h3><p>Lorem Ipsum is simply dummy text of the printing and typesetting industry.</p><span class="link">Read More</span></div>
      </article>
      <article class="proj-card">
        <div role="img" aria-label="Photo of workers loading crates of produce near a tractor" style="height:186px;background:linear-gradient(180deg,#6e9cc8 0%,#567b3b 45%,#8a5a3a 100%)"></div>
        <div class="body"><h3>PROCESSING AND<br>DISTRIBUTION</h3><p>Lorem Ipsum is simply dummy text of the printing and typesetting industry.</p><span class="link">Read More</span></div>
      </article>
    </div>
    <div class="center" style="margin-top:28px"><span class="btn">Contact Us</span></div>
  </div>
</section>

<section class="reviews">
  <div class="half" role="img" aria-label="Photo of women hoeing crops in a field" style="background:linear-gradient(135deg,#8c7a45 0%,#6b6a34 40%,#4f6a2a 70%,#8a7a52 100%)"></div>
  <div class="half review-panel">
    <h2>CUSTOMER REVIEWS</h2>
    <p>"Sed ut perspiciatis unde omnis iste natus error sit voluptatem accusantium doloremque laudantium, totam rem aperiam, ex eaque ipsa quae ab illo inventore veritatis et quasi architecto beatae vitae dicta sunt explicabo. Nemo enim ipsam."</p>
    <div class="reviewer">
      <div class="avatar" role="img" aria-label="Reviewer portrait"></div>
      <div><b>Tomas Kerr</b><span class="stars">★★★★★</span></div>
    </div>
  </div>
</section>

<section class="zones">
  <div class="zones-text">
    <h2>AGRICULTURAL<br>PRODUCTION ZONES</h2>
    <p class="lead">Ut enim ad minim veniam, quis nostrud exercitation ullamco laboris nisi ut aliquip ex ea commodo consequat.</p>
    <ul class="legend">
      <li><i style="background:var(--green)"></i>Farming Zones</li>
      <li><i style="background:var(--tan)"></i>Local Farmer Assistance</li>
      <li><i style="background:var(--blue)"></i>Processing and Distribution</li>
    </ul>
    <span class="btn">Contact Us</span>
  </div>
  <div class="map" role="img" aria-label="Map of Namibia divided into regions coloured green for farming zones, tan for local farmer assistance and blue for processing and distribution" style="width:400px;height:408px;background:linear-gradient(160deg,var(--green) 0%,var(--green) 30%,var(--blue) 45%,var(--tan) 55%,var(--blue) 65%,var(--green) 78%,var(--green) 100%);border-radius:6px"></div>
</section>

<section class="stats">
  <div class="stat" role="img" aria-label="Photo of a green crop field under a blue sky" style="background:linear-gradient(180deg,#1c4f9a 0%,#4f87c5 45%,#3f7a2a 70%,#2c5a1e 100%)">
    <div class="num">75%</div><div class="label">Hectares Of Land Cultivated</div>
  </div>
  <div class="stat" role="img" aria-label="Photo of a farmer working among green crops" style="background:linear-gradient(180deg,#4f8a5a 0%,#3d7a48 50%,#2f6a3a 100%)">
    <div class="num">25%</div><div class="label">Farmers Assisted</div>
  </div>
  <div class="stat" role="img" aria-label="Photo of grain silos beside a field" style="background:linear-gradient(180deg,#8a9c8a 0%,#5f7a5e 45%,#2f6a2e 100%)">
    <div class="num">85%</div><div class="label">Reduction In Food Imports</div>
  </div>
</section>

<section class="news">
  <div class="wrap">
    <h2 class="section-title">LATEST NEWS AND UPDATES</h2>
    <p class="section-lead">Lorem ipsum dolor sit amet, consectetur adipiscing elit, sed do eiusmod tempor incididunt ut labore et dolore magna aliqua.</p>
    <div class="arrow" style="left:-66px;top:322px"><svg width="10" height="12" viewBox="0 0 10 12"><path d="M7 1L2 6l5 5" fill="none" stroke="#111" stroke-width="2"/></svg></div>
    <div class="arrow" style="right:-66px;top:322px"><svg width="10" height="12" viewBox="0 0 10 12"><path d="M3 1l5 5-5 5" fill="none" stroke="#111" stroke-width="2"/></svg></div>
    <div class="news-cards">
      <article class="news-card">
        <div role="img" aria-label="Photo of a farmer tending crops in a field" style="height:206px;background:linear-gradient(180deg,#6f8f4a 0%,#4d7a2e 50%,#3a6022 100%)"></div>
        <div class="body"><div class="date">10, June 2024</div><h4>Lorem ipsum dolor sit ametco adipiscing eliter sed diam</h4><p>Lorem ipsum dolor sit ametewroe ctetuer adipiscing eliter sed diam utlaoreeteere sed diam</p><span class="link">Read More</span></div>
      </article>
      <article class="news-card">
        <div class="body"><div class="date">28, May 2024</div><h4>Lorem ipsum dolor sit ametco adipiscing eliter sed diam</h4><p>Lorem ipsum dolor sit ametewroe ctetuer adipiscing eliter sed diam utlaoreeteere sed diam</p><span class="link">Read More</span></div>
        <div role="img" aria-label="Photo of a wheat field with solar panels" style="height:206px;margin-top:10px;background:linear-gradient(180deg,#5b8fd1 0%,#9cc0e6 25%,#7fa860 40%,#5c8a35 100%)"></div>
      </article>
      <article class="news-card">
        <div role="img" aria-label="Photo of two farmers holding a basket of harvest in a maize field" style="height:206px;background:linear-gradient(90deg,#5a7a2e 0%,#9a8a40 50%,#4a6a26 100%)"></div>
        <div class="body"><div class="date">14, April 2024</div><h4>Lorem ipsum dolor sit ametco adipiscing eliter sed diam</h4><p>Lorem ipsum dolor sit ametewroe ctetuer adipiscing eliter sed diam utlaoreeteere sed diam</p><span class="link">Read More</span></div>
      </article>
    </div>
    <div class="center" style="margin-top:30px"><span class="btn">View All News And Updates</span></div>
  </div>
</section>

<section class="newsletter">
  <div class="nl-box">
    <div class="nl-art" role="img" aria-label="Illustration of a young plant with a water droplet above a crop field"></div>
    <div class="nl-content">
      <h2>NEWSLETTER SIGN UP</h2>
      <p>Sed ut perspiciatis unde omnis iste natus error sit voluptatem accusantium doloremque laudantium, totam rem aperiam.</p>
      <div class="nl-form"><div class="input">Enter Your Email Address</div><div class="sub">Subscribe</div></div>
    </div>
  </div>
</section>

<footer>
  <div class="footer">
    <div class="quick">
      <h5>QUICK LINKS</h5>
      <ul><li>• Home</li><li>• About Us</li><li>• Our Projects</li><li>• Farmer Resources</li><li>• News &amp; Updates</li><li>• Contact Us</li></ul>
    </div>
    <div class="foot-brand"><i></i>Meridale Field Trust</div>
    <div class="contact">
      <h5>CONTACT DETAILS</h5>
      <div class="row"><div class="ico"><svg width="12" height="14" viewBox="0 0 12 14"><path d="M6 13S1 8 1 5a5 5 0 0 1 10 0c0 3-5 8-5 8z" fill="#fff"/><circle cx="6" cy="5" r="2" fill="#333"/></svg></div><div>48, Field House, Harvest Road,<br>Region QX 204518</div></div>
      <div class="row"><div class="ico"><svg width="13" height="10" viewBox="0 0 13 10"><rect width="13" height="10" fill="#fff"/><path d="M0 0l6.5 5L13 0" fill="none" stroke="#333"/></svg></div><div>Email<br>info@meridalefieldtrust.org</div></div>
      <div class="row"><div class="ico"><svg width="12" height="12" viewBox="0 0 12 12"><path d="M2 1l2 0 1 3-1.5 1a7 7 0 0 0 3.5 3.5L8 7l3 1v2a1 1 0 0 1-1 1A9 9 0 0 1 1 2a1 1 0 0 1 1-1z" fill="#fff"/></svg></div><div>Phone<br>555-014-2290</div></div>
    </div>
  </div>
  <div class="bottom">
    <div class="wrap">
      <span>©2024 Meridale Field Trust. All Rights Reserved.</span>
      <div class="socials" aria-label="Social links"><span></span><span></span><span></span><span></span></div>
    </div>
  </div>
</footer>

</body>
</html>
```